Vehicle Wrap

Looking for a new design to our electrical vans. Partial wrap , sides and back - no front. Logo , Services offered , KPB & RMO # , phone number and website. Needs to Use Vorlund logo as well.

```html
<!DOCTYPE html>
<html lang="en">
<head>
<meta charset="utf-8">
<title>Harbour Electric – Van Side Wrap</title>
<link rel="stylesheet" href="https://fonts.googleapis.com/css2?family=Oswald:wght@600&family=Roboto:wght@400;700;900&display=swap">
<style>
  :root {
    --wrap-black: #050505;
    --wrap-white: #f4f4f4;
    --front-light: #ffffff;
    --front-grey: #dcdcdc;
    --brand-gold: #d4a11e;
    --text-white: #ffffff;
    --text-dark: #111111;
  }
  * { margin: 0; padding: 0; box-sizing: border-box; }
  html, body {
    width: 1200px; height: 566px; overflow: hidden;
    background: #ffffff;
    font-family: "Roboto", Arial, sans-serif;
  }
  .wrap-panel {
    position: relative;
    width: 1200px; height: 566px;
    overflow: hidden;
  }
  .front-section {
    position: absolute;
    left: 0; top: 0;
    width: 640px; height: 566px;
    background: linear-gradient(90deg, var(--front-light), var(--front-grey));
  }
  .rear-section {
    position: absolute;
    left: 640px; top: 0;
    width: 560px; height: 566px;
    background: var(--wrap-black);
  }
  .brand-badge {
    position: absolute;
    left: 429px; top: 49px;
    width: 416px; height: 416px;
    border-radius: 50%;
    background: var(--wrap-black);
    display: flex; align-items: center; justify-content: center;
    text-align: center;
  }
  .brand-name {
    font-family: "Roboto", Arial, sans-serif;
    font-weight: 900;
    color: var(--brand-gold);
    font-size: 54px;
    line-height: 1.02;
    letter-spacing: 2px;
  }
  .contact-block {
    position: absolute;
    left: 850px; top: 178px;
    width: 240px;
    text-align: center;
  }
  .phone {
    font-family: "Oswald", "Arial Narrow", sans-serif;
    font-weight: 600;
    font-size: 35px;
    color: var(--text-white);
    letter-spacing: 0.5px;
    line-height: 1.1;
  }
  .website {
    font-size: 17px;
    color: var(--brand-gold);
    margin-top: 2px;
  }
  .service-list {
    list-style: none;
    margin-top: 14px;
    font-size: 10.5px;
    font-weight: 700;
    color: var(--text-white);
    line-height: 13.7px;
    white-space: nowrap;
  }
  .service-list li::before {
    content: "";
    display: inline-block;
    width: 6px; height: 6px;
    border-radius: 50%;
    background: var(--brand-gold);
    margin-right: 7px;
    vertical-align: 1px;
  }
  .dealer-tag {
    position: absolute;
    left: 295px; top: 300px;
    width: 76px;
    background: var(--text-white);
    border: 1px solid var(--text-dark);
    border-radius: 3px;
    text-align: center;
  }
  .dealer-name {
    background: var(--text-dark);
    color: var(--text-white);
    font-weight: 700;
    font-size: 11px;
    letter-spacing: 0.5px;
    padding: 3px 0 4px;
  }
  .dealer-role {
    font-size: 5.5px;
    font-weight: 700;
    color: var(--text-dark);
    padding: 3px 0;
  }
  .licence-numbers {
    position: absolute;
    left: 322px; top: 351px;
    font-size: 7px;
    font-weight: 700;
    color: var(--text-dark);
    line-height: 9px;
    text-align: center;
  }
</style>
</head>
<body>
<main class="wrap-panel">
  <div class="front-section"></div>
  <div class="rear-section"></div>

  <div class="brand-badge">
    <div class="brand-name">HARBOUR<br>ELECTRIC</div>
  </div>

  <div class="dealer-tag">
    <div class="dealer-name">VORLUND</div>
    <div class="dealer-role">SALES &amp; SERVICE DEALER</div>
  </div>

  <div class="licence-numbers">
    KPB# 7004821<br>RMO# 000512384
  </div>

  <div class="contact-block">
    <div class="phone">555-014-2290</div>
    <div class="website">HarbourElectric.ca</div>
    <ul class="service-list">
      <li>VORLUND SERVICE &amp; SALES</li>
      <li>EV CHARGER INSTALLATIONS</li>
      <li>RESIDENTIAL &amp; COMMERCIAL SERVICES</li>
      <li>GAS &amp; ELECTRICAL</li>
    </ul>
  </div>
</main>
</body>
</html>
```